Business Brochure Design Project

BRIGHTFERN VENTURE SERVICES
Our company requires a business brochure designed, this design will be printed and emailed to prospective corporate clients to provide an understanding of our businesses services. The written content required in this brochure is attached as a word document.

DESIGN
The design needs to hold your attention and identify the company brand. An A4 portrait format will be used with a white background. Brochure pages will never be viewed side by side as most clients will recieve this as a pdf document attached to an email so considered this in your design. Colour graphics and images will be used to enhance the content and draw people in. To reflect quality, only high resolution images that are clear, sharp and in focus will be used. Please use the CMYK colour model when designing as this brochure will also be printed.

LOOK AND FEEL
The design needs to be savvy, appear uncluttered and have an attitude of a market leader. I want something that stands out in the crowd and effectively markets my businesses brand. It needs to be elegant, modern and have a corporate feel. I want something that has energy, is fresh, innovative, exciting and inviting.

FINISHED PRODUCT
All content in the photo shop design needs to be fully editable including text. Our business has a copy of photo shop CS6, so the finished product must be compatible with this version of software. Each page must contain the text “Copyright © 2013 Brightfern Venture Services. All rights reserved”
Updates

Hi all

I will also be setting up a stationay project soon, if your are interested in being part of it please let me know.

Thanks

                          

I like designs that use a white background with the use of red, black and grey colours within

 

To all designers

Thanks for the great design work; I look forward to working with you all again in the future

 

Regards Marcus Delaney

Industry/Entity Type

Shop

Requirements
Must have
• This design must be professional and of the highest calibre

Please use the CMYK colour model as this is the formatt by printers.

Business contact details must be clearly visible on the cover page
Should not have
• Each part of my business advertising needs to look interesting in its own right. This insures companies are intrigued to find out more about our services, who we are and what we do. Please do not design something that looks identical to my webpage site or Facebook page. Your design needs to adds value to the overall promotional impact of my business.

The design should not be based off a generic design template, it needs to be unique.

```html
<!DOCTYPE html>
<html lang="en">
<head>
<meta charset="utf-8">
<title>Brightfern Venture Services – Business Profile</title>
<link rel="stylesheet" href="https://fonts.googleapis.com/css2?family=Arimo:wght@400;700&family=Josefin+Sans:wght@600&family=Tinos:wght@700&display=swap">
<style>
  :root {
    --ink: #111111;
    --charcoal: #2b2b2b;
    --grey: #8f9597;
    --red: #e3161b;
    --deep-red: #9c1a1a;
    --blush: #f6c3c3;
    --paper: #ffffff;
  }
  html, body {
    margin: 0;
    padding: 0;
    overflow: hidden;
    background: var(--paper);
  }
  .cover {
    position: relative;
    width: 849px;
    height: 1200px;
    overflow: hidden;
    background: var(--paper);
    font-family: "Arimo", Arial, sans-serif;
  }
  .top-band {
    position: absolute;
    left: 0; top: 0;
    width: 849px; height: 62px;
    background: linear-gradient(90deg, var(--charcoal) 0%, #5d6264 35%, #b9bebf 70%, var(--paper) 100%);
  }
  .top-band::after {
    content: "";
    position: absolute;
    left: 0; right: 0; bottom: 0;
    height: 14px;
    background: linear-gradient(90deg, #a7adaf 0%, #d9dcdd 60%, var(--paper) 100%);
  }
  .backdrop {
    position: absolute;
    left: 0; top: 280px;
    width: 849px; height: 660px;
    background:
      radial-gradient(ellipse 60% 45% at 65% 40%, rgba(240,140,140,0.45), rgba(255,255,255,0) 70%),
      radial-gradient(ellipse 45% 35% at 20% 55%, rgba(240,150,150,0.35), rgba(255,255,255,0) 70%);
  }
  .brand {
    position: absolute;
    left: 125px; top: 190px;
    width: 600px;
  }
  .brand-name {
    display: flex;
    align-items: center;
    gap: 14px;
    margin: 0;
    font-family: "Arimo", Arial, sans-serif;
    font-weight: 700;
    font-size: 33px;
    letter-spacing: -0.5px;
    color: var(--ink);
  }
  .brand-mark {
    width: 40px; height: 40px;
    background: var(--red);
    flex: none;
  }
  .brand-tagline {
    margin: 8px 0 0 54px;
    font-size: 15px;
    font-weight: 700;
    color: var(--ink);
  }
  .title {
    position: absolute;
    left: 0; top: 352px;
    width: 849px;
    margin: 0;
    text-align: center;
    font-family: "Josefin Sans", "Century Gothic", sans-serif;
    font-weight: 600;
    font-size: 60px;
    line-height: 84px;
    letter-spacing: 1px;
    color: var(--ink);
  }
  .subtitle {
    position: absolute;
    left: 100px; top: 596px;
    width: 649px;
    margin: 0;
    text-align: center;
    font-family: "Tinos", "Times New Roman", serif;
    font-weight: 700;
    font-size: 22px;
    line-height: 31px;
    text-transform: uppercase;
    color: var(--deep-red);
  }
  .footer-wave {
    position: absolute;
    left: 0; top: 975px;
    width: 849px; height: 225px;
  }
  .contact {
    position: absolute;
    left: 0; top: 1075px;
    width: 849px;
    margin: 0;
    text-align: center;
    font-style: normal;
    font-size: 10.5px;
    line-height: 13px;
    color: var(--paper);
  }
  .contact p { margin: 0; }
  .contact .label { text-transform: uppercase; }
</style>
</head>
<body>
<main class="cover">
  <div class="top-band"></div>

  <div class="backdrop" role="img" aria-label="Soft pale red background wash of overlapping translucent tiles"></div>

  <header class="brand">
    <p class="brand-name"><span class="brand-mark"></span>BRIGHTFERN VENTURE SERVICES</p>
    <p class="brand-tagline">Providing Effective Project Controls and Management Solutions</p>
  </header>

  <h1 class="title">BRIGHTFERN VENTURE<br>SERVICES<br>BUSINESS PROFILE</h1>

  <h2 class="subtitle">Providing effective project controls and management solutions within Australia and overseas</h2>

  <svg class="footer-wave" viewBox="0 0 849 225" preserveAspectRatio="none" aria-hidden="true">
    <defs>
      <linearGradient id="wave-grey" x1="0" y1="0" x2="1" y2="0">
        <stop offset="0" stop-color="#3a3a3a"/>
        <stop offset="0.6" stop-color="#262626"/>
        <stop offset="1" stop-color="#555a5c"/>
      </linearGradient>
    </defs>
    <path d="M0 40 C 200 10, 560 0, 849 5 L 849 225 L 0 225 Z" fill="url(#wave-grey)"/>
    <path d="M0 55 C 250 30, 600 25, 849 28 L 849 225 L 0 225 Z" fill="#1a1a1a"/>
    <path d="M0 72 C 260 48, 600 45, 849 52 L 849 225 L 0 225 Z" fill="#e3161b"/>
  </svg>

  <address class="contact">
    <p class="label">Contract Details</p>
    <p>DIRECTOR:&nbsp; MARCUS DELANEY</p>
    <p>MOB: +61 0400555182&nbsp; WEBSITE: www.brightfernventures.com.au</p>
    <p>EMAIL: marcus@brightfernventures.com.au&nbsp; LINKDEN: www.linkedin.com/in/mdelaneybrightfern&nbsp;FACE</p>
    <p>BOOK: www.facebook.com/BrightfernVenturesGlobal</p>
  </address>
</main>
</body>
</html>
```